Renny Osbert Personalised Health, Performance and Longevity Exec Coach

Business Card for www.rennyosbert.example site. It is a trust site and I use it for 1:1 relatable connections. It is the one I use for building intimate 1:1 trust building and Exec Coaching Services and programs for high wealth individuals and corporates. I also have a commercial programmatic site of my personal health products and services and programs for main stream one to many. www.halfwaypioneer.example that can also provoke thought for the www.rennyosbert.example business card. (mind you will get a separate business card for that site, but want to provide context). It has a logo which you may want to draw from in designing the rennyosbert business card which is personal and is about building my brand. There is also a rennyosbert personal Chirply page and rennyosbert business Chirply page. I am a Certified Talent Compass 3.1 Coach with Verrow and you can get a corporate brief of me on there to give you more context https://www.verrowtalenthub.example/coach/en-us/directory?search=renny

Target Market(s)

Being a Personalised Health Coach I am focused on Health>Performance>Longevity>Wellbeing. Target market is Executives /High Wealth individuals/Corporates. I am most relatable to the IT industry as I was ion it building partnerships for IT companies for 28+ years.

Industry/Entity Type

Health And Wellness

Contact Information for Business Card

Name: Renny Osbert
email: renny@rennyosbert.example
Phone: Australia +61 491352864 Singapore +65 83426109

Font styles to use
Sans Serif
Other font styles liked:
• Arial and Calibra could work?

Colors

Designer to choose colors to be used in the design.

Requirements
Must have
• It must be a no BS design that is intimate. In keeping with the rennyosbert.example website I'm guessing grey scale. It may be printed on plastic as well for durability and a point of difference. It must have people feeling trust and feeling safe to be 1:1 personal. It's about helping people move from stuck to sustainable change. Moving them to a healthier state, increasing performance if and where they want, longevity and well being.
Nice to have
• On the back you can place a logo that is in line with what I have as a colourful mandala at www.halfwaypioneer.example. It will be on the landing page and top left of each page in that site. A greyscale simpler version to create linkage to my philosophy. Also you could have the continuum of Personalised Health > > Performance > Longevity > Wellbeing as well or instead of in your designs some how infographcially represented if not using the existing logo at Halfwaypioneer.example
Should not have
• Clutter is a no no. Keep it clean, easy to read, no BS feel. Must be authentic and warm yet smart.

```html
<!DOCTYPE html>
<html lang="en">
<head>
<meta charset="UTF-8">
<title>Renny Osbert – Business Card</title>
<link rel="stylesheet" href="https://fonts.googleapis.com/css2?family=Arimo:wght@400;700&display=swap">
<style>
  :root {
    --stage: #2b2b2e;
    --card-front: #121212;
    --card-back: #161616;
    --ink: #ffffff;
    --ink-soft: #e4e4e4;
    --photo-light: #bdbdbd;
    --photo-mid: #6e6e6e;
    --photo-dark: #161616;
  }
  * { box-sizing: border-box; margin: 0; padding: 0; }
  html, body {
    width: 1200px; height: 800px; overflow: hidden;
    background: var(--stage);
    font-family: "Arimo", Arial, sans-serif;
    color: var(--ink);
  }
  .stage {
    position: relative; width: 1200px; height: 800px;
  }
  .card {
    position: absolute;
    width: 560px; height: 320px;
    overflow: hidden;
    box-shadow: 0 14px 30px rgba(0,0,0,0.45);
  }
  .card--front {
    left: 90px; top: 60px;
    background: var(--card-front);
    display: flex; align-items: center; justify-content: center;
  }
  .front-name {
    font-weight: 700; font-size: 34px; letter-spacing: 1px;
    text-transform: uppercase;
    transform: translate(-20px, 30px);
  }
  .card--back {
    left: 550px; top: 420px;
    background: var(--card-back);
  }
  .portrait {
    position: absolute; left: 0; bottom: 0;
    width: 330px; height: 240px;
    background:
      radial-gradient(ellipse at 35% 70%, var(--photo-light) 0%, var(--photo-mid) 45%, transparent 80%),
      linear-gradient(30deg, var(--photo-mid) 0%, #3a3a3a 55%, var(--photo-dark) 100%);
  }
  .details {
    position: absolute; left: 350px; top: 44px;
    width: 200px;
  }
  .details-name {
    font-weight: 700; font-size: 16px; text-transform: uppercase; letter-spacing: 0.4px;
  }
  .details-title {
    font-size: 12.5px; color: var(--ink-soft); margin-top: 2px;
  }
  .region { margin-top: 24px; }
  .region + .region { margin-top: 18px; }
  .region-label { font-weight: 700; font-size: 13px; }
  .region-phone { font-size: 13px; color: var(--ink-soft); margin-top: 2px; }
  .links { margin-top: 26px; list-style: none; }
  .links li {
    display: flex; align-items: center; gap: 7px;
    font-size: 12px; color: var(--ink-soft); line-height: 17px;
  }
  .links svg { width: 11px; height: 11px; flex: none; }
</style>
</head>
<body>
<main class="stage">
  <section class="card card--front" aria-label="Card front">
    <h1 class="front-name">Renny Osbert</h1>
  </section>

  <section class="card card--back" aria-label="Card back">
    <div class="portrait" role="img" aria-label="Black and white photograph of the coach standing beside palm leaves in a colonnade"></div>
    <div class="details">
      <p class="details-name">Renny Osbert</p>
      <p class="details-title">Certified Talent Compass Coach</p>

      <div class="region">
        <p class="region-label">Australia</p>
        <p class="region-phone">+61 491352864</p>
      </div>
      <div class="region">
        <p class="region-label">Singapore</p>
        <p class="region-phone">+65 83426109</p>
      </div>

      <ul class="links">
        <li>
          <svg viewBox="0 0 12 12" aria-hidden="true"><rect x="0.5" y="2" width="11" height="8" fill="#fff"/><path d="M0.5 2 L6 6.5 L11.5 2" fill="none" stroke="#161616" stroke-width="1"/></svg>
          renny@rennyosbert.example
        </li>
        <li>
          <svg viewBox="0 0 12 12" aria-hidden="true"><circle cx="6" cy="6" r="5.5" fill="#fff"/><g fill="none" stroke="#161616" stroke-width="0.8"><ellipse cx="6" cy="6" rx="2.3" ry="5.2"/><line x1="0.6" y1="6" x2="11.4" y2="6"/><line x1="1.5" y1="3.5" x2="10.5" y2="3.5"/><line x1="1.5" y1="8.5" x2="10.5" y2="8.5"/></g></svg>
          www.rennyosbert.example
        </li>
      </ul>
    </div>
  </section>
</main>
</body>
</html>
```